Christmas Banner for frontpage of website

New online scarf store just opened needs a Christmas Banner stating Free Delivery (UK only). Also if it could incorporate guaranteed Christmas delivery if ordered before 18th (might be too wordy though?) I would really like it to bring some colour to the page. The page is currently black and white with a pink accent and is very simple which is why I would like something modern and elegant, simple but with some colour. It is a shopify store I understand the banner size should be 950px by 290px the website is www.velmorrow.co.uk

Target Market(s)

Ladies

Industry/Entity Type

Store

Requirements
Should not have
• Not to look tacky.

```html
<!DOCTYPE html>
<html lang="en">
<head>
<meta charset="utf-8">
<title>Velmorrow – Christmas Free Delivery Banner</title>
<link rel="stylesheet" href="https://fonts.googleapis.com/css2?family=Great+Vibes&family=Dancing+Script:wght@500&family=Handlee&display=swap">
<style>
  :root {
    --snow-light: #f7f7f8;
    --snow-mid: #e4e6ea;
    --wood-shade: #c9ccd2;
    --scarf-grey: #9aa3ad;
    --scarf-dark: #7d8792;
    --tangerine: #e8781e;
    --tangerine-light: #f3a04a;
    --leaf-green: #4f7a3a;
    --title-red: #b23b47;
    --accent-pink: #e48580;
    --body-ink: #3a3436;
  }
  * { margin: 0; padding: 0; box-sizing: border-box; }
  html, body {
    width: 1200px;
    height: 365px;
    overflow: hidden;
    background: var(--snow-light);
  }
  .banner {
    position: relative;
    width: 1200px;
    height: 365px;
    overflow: hidden;
  }
  .banner__backdrop {
    position: absolute;
    inset: 0;
    background:
      radial-gradient(ellipse 55% 70% at 50% 48%, var(--snow-light) 0%, rgba(247,247,248,0.6) 60%, rgba(247,247,248,0) 100%),
      linear-gradient(180deg, var(--snow-mid) 0%, var(--snow-light) 45%, var(--wood-shade) 100%);
  }
  .banner__scarf-photo {
    position: absolute;
    left: 0;
    top: 0;
    width: 330px;
    height: 365px;
    background:
      radial-gradient(circle at 150px 95px, var(--tangerine-light) 0, var(--tangerine) 42px, rgba(232,120,30,0) 44px),
      radial-gradient(ellipse 120px 150px at 140px 210px, var(--scarf-grey) 0%, var(--scarf-dark) 70%, rgba(125,135,146,0) 100%);
  }
  .banner__tangerine-photo {
    position: absolute;
    right: 0;
    top: 0;
    width: 220px;
    height: 365px;
    background:
      radial-gradient(circle at 70px 40px, var(--leaf-green) 0, var(--leaf-green) 30px, rgba(79,122,58,0) 34px),
      radial-gradient(circle at 185px 155px, var(--leaf-green) 0, var(--leaf-green) 34px, rgba(79,122,58,0) 38px),
      radial-gradient(circle at 165px 260px, var(--tangerine-light) 0, var(--tangerine) 50px, rgba(232,120,30,0) 53px);
  }
  .banner__copy {
    position: absolute;
    left: 0;
    right: 0;
    top: 0;
    text-align: center;
  }
  .banner__store-name {
    position: absolute;
    left: 0;
    right: 0;
    top: 42px;
    font-family: "Great Vibes", cursive;
    font-weight: 400;
    font-size: 132px;
    line-height: 1;
    color: var(--title-red);
  }
  .banner__offer {
    position: absolute;
    left: 0;
    right: 0;
    top: 178px;
    font-family: "Dancing Script", cursive;
    font-weight: 500;
    font-size: 48px;
    line-height: 1;
    color: var(--accent-pink);
  }
  .banner__offer-note {
    font-size: 30px;
  }
  .banner__snowflake {
    display: inline-block;
    width: 30px;
    height: 30px;
    margin-left: 10px;
    vertical-align: 2px;
    background: var(--accent-pink);
    opacity: 0.35;
    border-radius: 50%;
  }
  .banner__guarantee {
    position: absolute;
    left: 0;
    right: 0;
    top: 252px;
    font-family: "Handlee", cursive;
    font-size: 27px;
    line-height: 1;
    color: var(--body-ink);
  }
  .banner__flourish {
    position: absolute;
    left: 520px;
    top: 314px;
    width: 300px;
    height: 20px;
    background: var(--title-red);
    opacity: 0.18;
    border-radius: 10px;
  }
</style>
</head>
<body>
  <div class="banner">
    <div class="banner__backdrop" role="img" aria-label="Snow-dusted white wooden boards"></div>
    <div class="banner__scarf-photo" role="img" aria-label="Grey knitted scarf wrapped around a tangerine on snowy wood"></div>
    <div class="banner__tangerine-photo" role="img" aria-label="Tangerines with green leaves on snowy wood"></div>

    <div class="banner__copy">
      <h1 class="banner__store-name">Velmorrow</h1>
      <p class="banner__offer">Free Delivery <span class="banner__offer-note">(UK only)</span><span class="banner__snowflake" role="img" aria-label="Snowflake ornament"></span></p>
      <p class="banner__guarantee">Guaranteed Christmas delivery if ordered before 18th</p>
    </div>

    <div class="banner__flourish" role="img" aria-label="Decorative swirl flourish with a small star"></div>
  </div>
</body>
</html>
```